Groundbreaking Automotive Product launch

Create a package insert for sample packs to be given away at industry trade show. The new product is an innovative automotive bumper protection system that is being introduced at a major trade show.

Fendrashield (www.fendrashield.biz) is a peel and stick clear film system that protects automobile bumpers from nicks, scratches, scrapes and scuffs. Our company is planning to sell the product to owners / operators of automated car wash businesses who will apply the product to car bumpers at the end of their normal wash cycle.

This package insert will be for sample packs that we will give away to car wash owners / operators at our trade show booth to encourage them to try the system on their own. The sample package (not for resale) includes 3 Fendrashield in a roll that is one inch in diameter and 5 inches high, one squeegee applicator (3 inch x 4 inch), and one 2 ounce bottle of spray lubricant ( 1 1/4 inch in diameter x 5 inches high). These contents will be contained in a clear plastic clamshell package. The insert is approximately 4 inches wide by 6 inches tall.

The face of the insert will not be obstructed by the package contents. it needs to contain the product logo (we will provide) and some attractive artwork showing the product in place on a car bumper - this needs to illustrate that the product is virtually invisible (except perhaps for a sparkle of sunlight off its highly polished surface) and does not change the appearance of the vehicle. The face of the insert will also require text indicating that product application helps them differentiate their car wash from the competition, is quick and easy without capital expense or staff training, can be done in a matter of seconds without disrupting the normal car wash process, preserves the appearance and resale value of the owner's vehicle, that the product is removable, the product is engineered to last up to one year, and that providing this bumper protection system can dramatically increase profits per transaction. Finally, our company contact information will also need to be included.

the back of the package insert will be obstructed partially by package contents but that does not affect insert design. the back of the insert merely needs to print application instructions (in black and white) which we will provide.
Updates

Project Deadline Extended

Target Market(s)

Owners / operators of automated car wash businesses located primarily in metropolitan areas.

Industry/Entity Type

Automotive

Requirements
Must have
• artwork must clearly indicate the product is applied to the flat surface of an automobile bumper while at the same time prominently featuring the product logo (we actually do print the logo design in one corner of the product itself).
Nice to have
• artwork that indicates the product is crystal clear and enhances the shine of the vehicle paint.
Should not have
• artwork should not suggest product is applied to bumper sections with dramatic or complex curves

```html
<!DOCTYPE html>
<html lang="en">
<head>
<meta charset="utf-8">
<title>Fendrashield – Package Insert</title>
<link rel="stylesheet" href="https://fonts.googleapis.com/css2?family=Mulish:ital,wght@0,400;0,600;0,700;0,800;0,900;1,700;1,800;1,900&display=swap">
<style>
  :root {
    --stage-light: #f4f4f4;
    --stage-dark: #cfcfcf;
    --wine-deep: #2a0507;
    --wine: #6e0b10;
    --wine-bright: #b3161d;
    --brand-red: #c21f25;
    --chrome: #e9e9e9;
    --chrome-dark: #8b8b8b;
    --banner-yellow: #f6c431;
    --banner-text: #1d5fb6;
    --white: #ffffff;
    --ink: #1e1e1e;
    --line-art: #d9d9d9;
    --badge-purple: #5a2f8f;
    --badge-yellow: #f2d200;
    --badge-blue: #1b8fd0;
    --badge-green: #3a9a35;
    --badge-red: #d8322c;
  }
  * { margin: 0; padding: 0; box-sizing: border-box; }
  html, body { width: 1200px; height: 900px; overflow: hidden; }
  body {
    position: relative;
    font-family: "Mulish", "Century Gothic", sans-serif;
    background: radial-gradient(ellipse at 50% 45%, var(--stage-light) 0%, var(--stage-dark) 100%);
  }

  /* ---------- Front of insert ---------- */
  .insert-front {
    position: absolute; left: 25px; top: 67px; width: 524px; height: 784px;
    border-radius: 5px; overflow: hidden;
    background:
      radial-gradient(ellipse 70% 55% at 30% 55%, var(--wine-bright) 0%, var(--wine) 45%, var(--wine-deep) 100%);
    box-shadow: 0 1px 4px rgba(0,0,0,.35);
    color: var(--white);
  }
  .corner-ribbon {
    position: absolute; left: -38px; top: 22px; width: 150px; height: 34px;
    background: var(--banner-yellow); transform: rotate(-45deg);
    color: var(--banner-text); text-align: center;
    font-weight: 800; font-style: italic; line-height: 1;
    padding-top: 2px;
  }
  .corner-ribbon small { display: block; font-size: 7px; }
  .corner-ribbon span { display: block; font-size: 11px; }
  .front-brand {
    position: absolute; right: 32px; top: 34px;
    font-size: 24px; font-weight: 700; letter-spacing: 2px; color: var(--brand-red);
  }
  .front-title {
    position: absolute; left: 32px; top: 86px; width: 480px;
    font-size: 34.5px; font-weight: 900; font-style: italic;
    color: #e6e6e6; text-shadow: 0 2px 4px rgba(0,0,0,.7);
    letter-spacing: -.2px; white-space: nowrap;
  }
  .front-copy {
    position: absolute; left: 12px;
    font-size: 11px; font-weight: 800; line-height: 1.12;
    white-space: nowrap;
  }
  .front-copy.intro { top: 149px; }
  .front-copy.details { top: 441px; }
  .hero-art { position: absolute; left: 0; top: 0; }
  .hero-tagline {
    position: absolute; left: 265px; top: 420px;
    font-size: 8.5px; font-weight: 600; white-space: nowrap;
  }
  .price-line {
    position: absolute; left: 0; width: 100%; top: 563px; text-align: center;
    font-size: 13.5px; font-weight: 700; font-style: italic;
  }
  .chrome-band {
    position: absolute; left: 0; width: 100%; height: 8px;
    background: linear-gradient(180deg, var(--chrome-dark), var(--chrome) 45%, var(--chrome-dark));
  }
  .chrome-band.upper { top: 590px; }
  .chrome-band.lower { top: 702px; }
  .feature-row {
    position: absolute; left: 15px; top: 612px; width: 495px;
    display: flex; justify-content: space-between;
  }
  .feature-badge {
    width: 77px; height: 76px; border-radius: 4px;
    border: 1px solid rgba(255,255,255,.8);
    display: flex; flex-direction: column; align-items: center; justify-content: space-between;
    padding: 5px 2px 4px; text-align: center;
  }
  .feature-badge p { font-size: 7.5px; font-weight: 700; font-style: italic; line-height: 1.05; }
  .feature-badge .numerals { font-size: 26px; font-weight: 800; font-style: italic; line-height: 1; margin-top: 4px; }
  .feature-badge .dollar { font-size: 34px; font-weight: 800; line-height: 1; }
  .feature-badge.easy { background: var(--badge-purple); }
  .feature-badge.tools { background: var(--badge-yellow); }
  .feature-badge.tools p { color: var(--white); text-shadow: 0 0 2px rgba(0,0,0,.5); }
  .feature-badge.year { background: linear-gradient(var(--badge-blue), #0f5f99); }
  .feature-badge.margin { background: var(--badge-green); }
  .feature-badge.exclusive { background: var(--badge-red); }
  .contact-block {
    position: absolute; left: 0; width: 100%; top: 717px; text-align: center;
    font-style: italic; font-weight: 700;
  }
  .contact-block .lead { font-size: 13px; }
  .contact-block .web, .contact-block .phone { font-size: 19px; font-weight: 800; line-height: 1.2; }

  /* ---------- Back of insert ---------- */
  .insert-back {
    position: absolute; left: 651px; top: 67px; width: 522px; height: 784px;
    background: var(--white); border-radius: 6px;
    box-shadow: 0 1px 3px rgba(0,0,0,.15);
    color: var(--ink);
  }
  .back-title { position: absolute; left: 27px; top: 50px; font-size: 20px; font-weight: 700; }
  .back-brand {
    position: absolute; right: 20px; top: 28px;
    font-size: 22px; font-weight: 700; letter-spacing: 2px; color: var(--brand-red);
  }
  .install-step { position: absolute; left: 0; width: 100%; }
  .step-number {
    position: absolute; left: 22px; width: 20px; height: 20px; border-radius: 50%;
    background: var(--ink); color: var(--white);
    font-size: 11px; font-weight: 800; text-align: center; line-height: 20px;
  }
  .step-drawing {
    position: absolute; left: 64px; width: 230px;
    background: linear-gradient(180deg, #f7f7f7, #ececec);
    border: 1px solid var(--line-art); border-radius: 4px;
  }
  .step-text {
    position: absolute; left: 336px;
    font-size: 13px; font-weight: 800; line-height: 1.08; white-space: nowrap;
  }
</style>
</head>
<body>

<section class="insert-front" aria-label="Front of package insert">
  <div class="corner-ribbon"><small>Exclusive</small><span>NEW</span><small>PRODUCT</small></div>
  <div class="front-brand">FENDRASHIELD</div>
  <h1 class="front-title">Invisible Bumper Protector</h1>

  <svg class="hero-art" width="524" height="784" viewBox="0 0 524 784" role="img" aria-label="Close-up of a glossy blue car bumper with the clear protective film catching a sparkle of light">
    <defs>
      <radialGradient id="paint" cx="0.3" cy="0.45" r="0.8">
        <stop offset="0" stop-color="#6b82d0"/>
        <stop offset=".5" stop-color="#2f44a0"/>
        <stop offset="1" stop-color="#18246a"/>
      </radialGradient>
      <linearGradient id="rim" x1="0" y1="0" x2="0" y2="1">
        <stop offset="0" stop-color="#f2f2f2"/>
        <stop offset=".5" stop-color="#7d7d7d"/>
        <stop offset="1" stop-color="#e0e0e0"/>
      </linearGradient>
    </defs>
    <ellipse cx="560" cy="318" rx="466" ry="172" fill="url(#rim)"/>
    <ellipse cx="563" cy="318" rx="459" ry="165" fill="url(#paint)"/>
    <ellipse cx="220" cy="288" rx="46" ry="36" fill="#8fd3f0" opacity=".55"/>
  </svg>

  <p class="front-copy intro">Imagine being the only car wash in the<br>neighbourhood to offer a quick, long<br>lasting solution to those annoying<br>nicks and scrapes on your<br>customers bumpers.</p>
  <p class="hero-tagline">FENDRASHIELD Product Can Increase Your Profit Margin!!!</p>
  <p class="front-copy details">FENDRASHIELD can be<br>quickly applied at the end of a<br>wash cycle. No special equipment is<br>needed and your staff need no special<br>training. Simply follow the three steps of<br>application as outlined on the back of this package.</p>

  <p class="price-line">Cost to you per application is only $27.45 but has a retail value of $49.99</p>

  <div class="chrome-band upper"></div>
  <div class="feature-row">
    <div class="feature-badge easy"><span class="numerals">1<sup>2</sup>3</span><p>Quick &amp; Easy<br>Application</p></div>
    <div class="feature-badge tools">
      <svg width="44" height="44" viewBox="0 0 44 44" aria-hidden="true"><circle cx="22" cy="22" r="18" fill="none" stroke="#111" stroke-width="4"/><line x1="9" y1="9" x2="35" y2="35" stroke="#111" stroke-width="4"/></svg>
      <p>No Special Tools<br>Required</p>
    </div>
    <div class="feature-badge year">
      <svg width="46" height="42" viewBox="0 0 46 42" aria-hidden="true">
        <rect x="1" y="1" width="44" height="40" fill="#fff" stroke="#111" stroke-width="2"/>
        <rect x="1" y="1" width="44" height="8" fill="#111"/>
        <path d="M1 17H45M1 25H45M1 33H45M9.8 9V41M18.6 9V41M27.4 9V41M36.2 9V41" stroke="#111" stroke-width="1.2"/>
      </svg>
      <p>Lasts up to 1 Year</p>
    </div>
    <div class="feature-badge margin"><span class="dollar">$</span><p>High Profit<br>Margin</p></div>
    <div class="feature-badge exclusive">
      <svg width="40" height="40" viewBox="0 0 40 40" aria-hidden="true"><rect x="11" y="4" width="18" height="24" fill="#fff"/><rect x="4" y="27" width="32" height="5" fill="#fff"/></svg>
      <p>Exclusive<br>Product</p>
    </div>
  </div>
  <div class="chrome-band lower"></div>

  <div class="contact-block">
    <p class="lead">For product and ordering information, visit</p>
    <p class="web">www.fendrashield.biz</p>
    <p class="phone">(743) 555-0142</p>
  </div>
</section>

<section class="insert-back" aria-label="Back of package insert">
  <h2 class="back-title">Installation Method</h2>
  <div class="back-brand">FENDRASHIELD</div>

  <div class="install-step" style="top:117px">
    <span class="step-number" style="top:16px">1</span>
    <div class="step-drawing" style="top:0;height:195px" role="img" aria-label="Line drawing of a rear bumper being washed with a sponge"></div>
    <p class="step-text" style="top:9px">Clean bumper with<br>any car wash soap<br>and water.</p>
  </div>

  <div class="install-step" style="top:338px">
    <span class="step-number" style="top:5px">2</span>
    <div class="step-drawing" style="top:0;height:200px" role="img" aria-label="Line drawing of a film sticker being sprayed with soap solution beside the bumper"></div>
    <p class="step-text" style="top:0">Select the correct size<br>film sticker for your<br>application, peel it<br>from the backing<br>paper, and spray the<br>side to be placed onto<br>the bumper with any<br>dilute mild soap<br>solution (such as Lumena<br>dishwashing soap)</p>
  </div>

  <div class="install-step" style="top:570px">
    <span class="step-number" style="top:6px">3</span>
    <div class="step-drawing" style="top:0;height:200px" role="img" aria-label="Line drawing of a squeegee smoothing the film onto the bumper"></div>
    <p class="step-text" style="top:1px">Place the film sticker<br>onto the bumper in the<br>desired location.<br>Starting from the<br>middle and moving<br>outward, use the<br>padded side fo the<br>squeegee to smooth<br>out all wrinkles and<br>bubbles.</p>
  </div>
</section>

</body>
</html>
```